Journeys With Marcella Business Cards

I need a business card design for my upscale Travel Agency.
Attached you can find my logo.
I would like to include the following:
- Name
- Title
- Phone Number
- Email
- Website
- and then something like: Follow us: JourneysWithMarcella (and then social media icons in color).
The logo should be in the front and then also the back.
I am also attaching a design that I liked (mostly for the layout) but open to any suggestions
Industry/Entity Type
Travel Agent
Contact Information for Business Card
Name: Marcella Dorn
Title: Travel Designer / Owner
Phone: 415-927-3308
Email: marcella@journeyswithmarcella-example.com
Website: www.JourneysWithMarcella-example.com
Social Media Handles for FB,IG, Twitter: JourneysWithMarcella
Colors
Designer to choose colors to be used in the design.
Look and feel

```html
<!DOCTYPE html>
<html lang="en">
<head>
<meta charset="utf-8">
<title>Journeys With Marcella – Business Cards</title>
<link rel="stylesheet" href="https://fonts.googleapis.com/css2?family=Montserrat:wght@400;500;600&display=swap">
<style>
  :root {
    --brand-orange: #f5a95a;
    --ink: #2f2f2f;
    --card: #ffffff;
    --backdrop: #e7e6e4;
  }
  * { box-sizing: border-box; margin: 0; padding: 0; }
  html, body { width: 1200px; height: 900px; overflow: hidden; }
  body {
    background: var(--backdrop);
    font-family: "Montserrat", Arial, sans-serif;
    color: var(--ink);
    position: relative;
  }
  .card {
    position: absolute;
    left: 220px;
    width: 760px;
    height: 410px;
    background: var(--card);
    border-radius: 18px;
    box-shadow: 0 6px 20px rgba(0,0,0,0.12);
    overflow: hidden;
  }
  .card--front { top: 25px; }
  .card--back { top: 465px; }

  .brand {
    display: flex;
    align-items: center;
    gap: 14px;
    color: var(--brand-orange);
    font-weight: 500;
    white-space: nowrap;
  }
  .brand__square {
    width: 40px; height: 40px;
    background: var(--brand-orange);
    flex-shrink: 0;
  }
  .card--front .brand {
    position: absolute;
    top: 160px; left: 0; right: 0;
    justify-content: center;
    font-size: 38px;
  }
  .front__web {
    position: absolute;
    bottom: 34px; left: 0; right: 0;
    text-align: center;
    font-size: 17px;
    letter-spacing: 0.5px;
  }

  .card--back .brand {
    position: absolute;
    top: 40px; left: 48px;
    font-size: 24px;
  }
  .card--back .brand__square { width: 30px; height: 30px; }

  .contact {
    position: absolute;
    top: 140px; left: 48px;
    width: 420px;
  }
  .contact__name {
    color: var(--brand-orange);
    font-weight: 600;
    font-size: 30px;
    letter-spacing: 1px;
    text-transform: uppercase;
    line-height: 1.1;
  }
  .contact__title { font-size: 19px; margin-bottom: 10px; }
  .contact__list { list-style: none; font-size: 16px; }
  .contact__list li { display: flex; align-items: center; gap: 10px; line-height: 1.6; white-space: nowrap; }
  .contact__list svg { width: 16px; height: 16px; flex-shrink: 0; }
  .contact__address { font-size: 18px; margin-top: 10px; line-height: 1.35; }

  .follow {
    position: absolute;
    top: 150px; right: 44px;
    display: flex; align-items: center; gap: 12px;
    font-size: 18px;
    white-space: nowrap;
  }
  .follow__square {
    width: 26px; height: 26px;
    border-radius: 5px;
    background: var(--brand-orange);
  }

  .back__mark {
    position: absolute;
    right: 44px; bottom: 40px;
    width: 230px;
    text-align: right;
    color: var(--brand-orange);
    font-weight: 500;
    font-size: 36px;
    line-height: 1.1;
  }
</style>
</head>
<body>
  <section class="card card--front">
    <div class="brand"><span class="brand__square"></span><span class="brand__name">Journeys With Marcella</span></div>
    <p class="front__web">www.JourneysWithMarcella-example.com</p>
  </section>

  <section class="card card--back">
    <div class="brand"><span class="brand__square"></span><span class="brand__name">Journeys With Marcella</span></div>

    <div class="follow">
      <span>Follow us: JourneysWithMarcella</span>
      <span class="follow__square"></span>
    </div>

    <div class="contact">
      <h1 class="contact__name">Marcella Dorn</h1>
      <p class="contact__title">Travel Designer / Owner</p>
      <ul class="contact__list">
        <li>
          <svg viewBox="0 0 16 16" aria-hidden="true"><path d="M4 1.5 L6 5 L4.5 6.5 Q6 10 9.5 11.5 L11 10 L14.5 12 L13 14.5 Q6 14 1.5 3 Z" fill="none" stroke="#f5a95a" stroke-width="1.4" stroke-linejoin="round"/></svg>
          <span>415-927-3308</span>
        </li>
        <li>
          <svg viewBox="0 0 16 16" aria-hidden="true"><rect x="1.5" y="3.5" width="13" height="9" fill="none" stroke="#f5a95a" stroke-width="1.4"/><path d="M1.5 3.5 L8 9 L14.5 3.5" fill="none" stroke="#f5a95a" stroke-width="1.4"/></svg>
          <span>marcella@journeyswithmarcella-example.com</span>
        </li>
        <li>
          <svg viewBox="0 0 16 16" aria-hidden="true"><circle cx="8" cy="8" r="6.5" fill="none" stroke="#f5a95a" stroke-width="1.4"/><ellipse cx="8" cy="8" rx="3" ry="6.5" fill="none" stroke="#f5a95a" stroke-width="1.2"/><path d="M1.5 8 H14.5" stroke="#f5a95a" stroke-width="1.2"/></svg>
          <span>www.JourneysWithMarcella-example.com</span>
        </li>
      </ul>
      <p class="contact__address">782 Willow Crest Lane<br>Brookmere, OR 97531</p>
    </div>

    <div class="back__mark">Journeys With Marcella</div>
  </section>
</body>
</html>
```